Need to create a website for a luxury custom home builder in Phoenix USA. Looking forward for some creative designs including a full page video intro on homepage and should show up pretty luxurious.

```html
<!DOCTYPE html>
<html lang="en">
<head>
<meta charset="utf-8">
<title>Stoneleigh Homes — Luxury Custom Home Builder</title>
<link rel="stylesheet" href="https://fonts.googleapis.com/css2?family=Cormorant+Garamond:wght@400;500&family=Montserrat:wght@400;500;600;700&display=swap">
<style>
:root{
  --ink:#0f3b3a;
  --teal:#0d3535;
  --blue:#1b8ad3;
  --text:#2d3b3b;
  --muted:#6f7777;
  --band:#eef0ef;
  --line:#c9cfcf;
  --white:#ffffff;
  --footer:#2b2b2b;
}
*{box-sizing:border-box;margin:0;padding:0}
html,body{width:1200px;height:4165px;overflow:hidden}
body{position:relative;background:var(--white);font-family:"Montserrat",sans-serif;color:var(--text)}
.section{position:absolute;left:0;width:1200px}
.badge{position:absolute;left:225px;height:15px;padding:0 12px;border-radius:8px;background:var(--teal);color:var(--white);font-size:9px;line-height:15px;font-weight:500}
.heading{position:absolute;left:225px;font-family:"Cormorant Garamond",serif;font-weight:500;font-size:38px;line-height:40px;color:var(--ink);letter-spacing:-.3px}
.lead{position:absolute;left:225px;font-size:10.5px;line-height:19px;color:var(--text)}
.arrow{position:absolute;width:36px;height:36px;border:1.5px solid var(--ink);border-radius:50%;display:flex;align-items:center;justify-content:center}

/* Hero */
.hero{top:0;height:594px;border-radius:0 0 130px 130px;overflow:hidden;
  background:linear-gradient(180deg,#3d4448 0%,#6d7479 30%,#9aa3a7 45%,#5a5d5c 65%,#2a2a2a 100%)}
.hero-photo{position:absolute;inset:0;background:
  radial-gradient(ellipse 260px 160px at 110px 450px,#c9a716 0%,#b39412 45%,transparent 75%),
  radial-gradient(ellipse 400px 200px at 520px 170px,#6f8a6b 0%,transparent 70%),
  linear-gradient(90deg,rgba(230,230,228,.35) 0%,transparent 30%,transparent 70%,rgba(240,240,238,.55) 100%)}
.nav{position:absolute;left:226px;top:32px;width:709px;height:60px;border-radius:30px;background:rgba(30,34,36,.82);display:flex;align-items:center;padding:0 22px 0 36px}
.brand{font-family:"Montserrat",sans-serif;font-weight:700;font-size:13px;letter-spacing:1px;color:var(--blue);display:flex;align-items:center;gap:6px}
.brand-dot{width:9px;height:9px;border-radius:50%;background:var(--blue)}
.nav-links{display:flex;margin-left:auto;align-items:center;gap:26px;font-size:9.5px;font-weight:500;color:var(--white)}
.nav-links .active{color:var(--blue);position:relative}
.nav-links .active::before{content:"";position:absolute;left:0;right:0;top:-21px;height:3px;background:var(--blue)}
.btn{display:inline-flex;align-items:center;justify-content:center;border-radius:16px;font-size:9.5px;font-weight:600;color:var(--white)}
.btn-blue{background:var(--blue)}
.btn-outline{border:1.5px solid var(--white)}
.hero-panel{position:absolute;left:225px;top:275px;width:750px;height:210px;border-radius:16px;background:rgba(28,28,28,.84)}
.hero-title{position:absolute;left:47px;top:48px;width:410px;white-space:nowrap;font-family:"Cormorant Garamond",serif;font-weight:400;font-size:42px;line-height:57px;color:var(--white);letter-spacing:0}
.hero-tag{position:absolute;left:478px;top:60px;font-size:11.5px;line-height:18px;color:var(--white)}
.hero-actions{position:absolute;left:478px;top:121px;display:flex;gap:14px}
.hero-actions .btn{width:106px;height:29px}

/* About */
.about{top:668px;height:477px}
.about-copy{position:absolute;left:225px;top:124px;width:380px;font-size:10.5px;line-height:19.5px;color:var(--text)}
.about-copy p{margin-bottom:19px}
.about-photo{position:absolute;left:699px;top:0;width:501px;height:401px;border-radius:18px 0 0 18px;background:linear-gradient(180deg,#5e7a5a 0%,#3c5238 35%,#4e6e3a 55%,#6f9a3f 80%,#5d8a34 100%)}
.about-detail{position:absolute;left:660px;top:263px;width:130px;height:149px;border-radius:6px;border:3px solid var(--white);background:linear-gradient(135deg,#e9e4de 0%,#d8cfc6 50%,#c9a99a 100%)}

/* Services */
.services{top:1145px;height:589px;background:var(--band);overflow:hidden}
.card{position:absolute;top:244px;width:243px;height:242px;background:var(--white);border-radius:10px}
.card.raised{height:273px;box-shadow:0 2px 6px rgba(0,0,0,.12)}
.card-icon{position:absolute;left:19px;top:30px;width:42px;height:42px;border-radius:50%;background:var(--blue);display:flex;align-items:center;justify-content:center}
.card h3{position:absolute;left:19px;top:92px;font-family:"Cormorant Garamond",serif;font-weight:500;font-size:18px;line-height:20px;color:var(--ink)}
.card p{position:absolute;left:19px;top:154px;width:190px;font-size:10px;line-height:19.5px;color:var(--text)}
.card.raised h3{top:94px}
.card.raised p{top:156px}

/* Portfolio */
.portfolio{top:1734px;height:588px;overflow:hidden}
.work{position:absolute;top:244px;width:243px;height:253px;border-radius:10px;overflow:hidden}
.work.tall{height:275px}
.work-label{position:absolute;left:12px;bottom:10px;padding:5px 10px;border-radius:6px;background:rgba(40,40,40,.72);color:var(--white);font-size:10px;line-height:14px}
.work-label b{font-weight:600}

/* FAQ */
.faq{top:2322px;height:650px;background:var(--band)}
.faq-box{position:absolute;left:225px;top:225px;width:750px;height:364px;background:var(--white);border-radius:16px}
.faq-item{position:absolute;left:25px;width:685px;height:58px;border-bottom:1px solid var(--line)}
.faq-q{position:absolute;left:0;font-family:"Cormorant Garamond",serif;font-weight:500;font-size:17px;color:var(--ink)}
.faq-toggle{position:absolute;right:0;width:20px;height:20px;border:1.3px solid var(--ink);border-radius:50%}
.faq-toggle::before,.faq-toggle.plus::after{content:"";position:absolute;left:5px;top:8.5px;width:8px;height:1.3px;background:var(--ink)}
.faq-toggle.plus::after{transform:rotate(90deg)}
.faq-a{position:absolute;left:0;top:62px;font-size:10px;line-height:19px;color:var(--text)}

/* Contact */
.contact{top:2972px;height:848px}
.sub-heading{position:absolute;left:225px;font-family:"Cormorant Garamond",serif;font-weight:500;font-size:21px;color:var(--ink)}
.info-bar{position:absolute;left:225px;top:289px;width:750px;height:97px;border-radius:49px;background:var(--blue);color:var(--white)}
.info{position:absolute;top:27px;display:flex;align-items:center;gap:16px}
.info-icon{width:42px;height:42px;border-radius:50%;background:var(--white);display:flex;align-items:center;justify-content:center;flex:none}
.info small{display:block;font-size:8px;opacity:.85;margin-bottom:3px}
.info strong{font-size:12px;font-weight:600;line-height:15px}
.form{position:absolute;left:225px;top:493px;width:640px;height:291px;background:var(--band);border-radius:16px}
.field-label{position:absolute;font-size:11px;color:var(--text)}
.field{position:absolute;height:30px;background:var(--white);border-radius:6px;font-size:10px;color:#9aa0a0;padding:9px 12px}
.submit{position:absolute;left:31px;top:231px;width:127px;height:28px;border-radius:14px;background:var(--blue);color:var(--white);font-size:10px;font-weight:600;display:flex;align-items:center;justify-content:center}

/* Footer */
.footer{top:3820px;height:345px;background:var(--footer);color:var(--white)}
.foot-links{position:absolute;top:63px;font-size:9.5px;line-height:31px}
.newsletter{position:absolute;right:225px;top:66px;text-align:right;font-size:10.5px;line-height:19px}
.subscribe{position:absolute;left:715px;top:114px;width:260px;height:36px;border-radius:18px;background:var(--white);color:var(--text);font-size:11px;padding:11px 18px}
.subscribe .btn{position:absolute;right:10px;top:6px;width:110px;height:24px;font-size:9.5px}
.socials{position:absolute;left:861px;top:163px;display:flex;gap:14px}
.socials span{width:18px;height:18px;border-radius:50%;background:var(--white)}
.foot-rule{position:absolute;left:225px;top:230px;width:750px;height:1px;background:#5a5a5a}
.foot-brand{position:absolute;left:225px;top:280px;font-size:15px}
.copyright{position:absolute;right:225px;top:284px;font-size:10px}
</style>
</head>
<body>

<section class="section hero">
  <div class="hero-photo" role="img" aria-label="Bright luxury living room with a yellow sofa, arc floor lamp and a wide window onto a mountain forest"></div>
  <nav class="nav">
    <div class="brand"><span class="brand-dot"></span>STONELEIGH</div>
    <div class="nav-links">
      <span class="active">HOME</span>
      <span>OUR SERVICES</span>
      <span>ABOUT STONELEIGH</span>
      <span>PORTFOLIO</span>
      <span class="btn btn-blue" style="width:106px;height:29px">CONTACT US</span>
    </div>
  </nav>
  <div class="hero-panel">
    <h1 class="hero-title">CRAFTING DREAMS,<br>BUILDING LUXURY</h1>
    <p class="hero-tag">Discover Unparalleled Luxury in Every<br>Corner of Your Custom-Built Home</p>
    <div class="hero-actions">
      <span class="btn btn-blue">CONTACT US</span>
      <span class="btn btn-outline">LEARN MORE</span>
    </div>
  </div>
</section>

<section class="section about">
  <span class="badge" style="top:9px">About US</span>
  <h2 class="heading" style="top:35px">Specialized in<br>Custom home building</h2>
  <div class="about-copy">
    <p>At Stoneleigh, we are more than just builders; we are dream weavers, visionaries, and artisans of luxury living.</p>
    <p>With a passion for creating unparalleled homes that reflect the unique aspirations of our clients, we have earned a reputation as a premier custom home builder.</p>
    <p>Your dream home is not just a structure; it's a statement of your identity and a testament to your success.</p>
    <p>When you choose Stoneleigh, you choose a partner committed to turning your dream into a luxurious living reality. We look forward to embarking on this journey with you.</p>
  </div>
  <div class="about-photo" role="img" aria-label="Large timber-framed manor house on a green lawn surrounded by forest"></div>
  <div class="about-detail" role="img" aria-label="Interior corner with a lamp, cushions and framed artwork"></div>
</section>

<section class="section services">
  <span class="badge" style="top:70px">Our Services</span>
  <h2 class="heading" style="top:84px">Experience the Extraordinary:<br>Your Luxury, Your Home.</h2>
  <p class="lead" style="top:176px">Your Dream, Our Blueprint: A Collaborative Design<br>Journey to Create a Home That Truly Represents You</p>
  <span class="arrow" style="left:873px;top:171px"><svg width="12" height="12" viewBox="0 0 12 12" fill="none" stroke="#0f3b3a" stroke-width="1.4"><path d="M10 6H2M5.5 2.5 2 6l3.5 3.5"/></svg></span>
  <span class="arrow" style="left:939px;top:171px"><svg width="12" height="12" viewBox="0 0 12 12" fill="none" stroke="#0f3b3a" stroke-width="1.4"><path d="M2 6h8M6.5 2.5 10 6 6.5 9.5"/></svg></span>

  <article class="card raised" style="left:225px">
    <span class="card-icon"><svg width="20" height="20" viewBox="0 0 20 20" fill="none" stroke="#fff" stroke-width="2" stroke-linecap="round"><path d="M4 16 12 8"/><circle cx="14" cy="6" r="3"/></svg></span>
    <h3>Custom Home<br>Design and Build</h3>
    <p>Our core expertise lies in crafting custom homes that are tailored to your unique vision. From the initial concept to the final finishing touches.</p>
  </article>
  <article class="card" style="left:479px">
    <span class="card-icon"><svg width="20" height="20" viewBox="0 0 20 20" fill="none" stroke="#fff" stroke-width="2" stroke-linecap="round"><path d="M3 17 17 3M6 14l2 2M9 11l2 2M12 8l2 2"/></svg></span>
    <h3>Architectural<br>Mastery</h3>
    <p>Our core expertise lies in crafting custom homes that are tailored to your unique vision. From the initial concept to the final...</p>
  </article>
  <article class="card" style="left:733px">
    <span class="card-icon"><svg width="20" height="20" viewBox="0 0 20 20" fill="none" stroke="#fff" stroke-width="2" stroke-linejoin="round"><path d="M3 16V10h14v6M5 10V7h10v3M3 16h14"/></svg></span>
    <h3>Interior Design<br>and Décor</h3>
    <p>Our core expertise lies in crafting custom homes that are tailored to your unique vision. From the initial concept to the final...</p>
  </article>
  <article class="card" style="left:987px">
    <span class="card-icon"><svg width="20" height="20" viewBox="0 0 20 20" fill="none" stroke="#fff" stroke-width="2" stroke-linejoin="round"><path d="M3 12a7 7 0 0 1 14 0zM2 12h16M10 5v3"/></svg></span>
    <h3>Construction and<br>Craftsmanship</h3>
    <p>Our core expertise lies in crafting custom homes that are tailored to your unique vision. From the initial concept to the final...</p>
  </article>
</section>

<section class="section portfolio">
  <span class="badge" style="top:71px">Our Portfolio</span>
  <h2 class="heading" style="top:84px">Discover Our<br>Masterpieces</h2>
  <p class="lead" style="top:176px">Welcome to our gallery of completed projects, where we take pride in<br>showcasing the exceptional homes we've crafted for our valued clients.</p>
  <span class="arrow" style="left:873px;top:171px"><svg width="12" height="12" viewBox="0 0 12 12" fill="none" stroke="#0f3b3a" stroke-width="1.4"><path d="M10 6H2M5.5 2.5 2 6l3.5 3.5"/></svg></span>
  <span class="arrow" style="left:939px;top:171px"><svg width="12" height="12" viewBox="0 0 12 12" fill="none" stroke="#0f3b3a" stroke-width="1.4"><path d="M2 6h8M6.5 2.5 10 6 6.5 9.5"/></svg></span>

  <div class="work tall" style="left:225px;background:linear-gradient(180deg,#9cc0de 0%,#e8e2d6 35%,#cdbfa8 55%,#3f8fb2 75%,#2c6f92 100%)" role="img" aria-label="White Mediterranean villa with arched windows reflected in a pool">
    <span class="work-label">The Serene Villa<br><b>Paradise Valley Retreat</b></span>
  </div>
  <div class="work" style="left:479px;background:linear-gradient(180deg,#6fb3e6 0%,#a9d2ef 35%,#8b7b66 55%,#d9d7d0 75%,#6e9a4a 100%)" role="img" aria-label="Two-storey suburban house with a garage and front lawn">
    <span class="work-label">Riverside Manor<br><b>Waterfront Elegance</b></span>
  </div>
  <div class="work" style="left:733px;top:247px;height:256px;background:linear-gradient(90deg,#e9e9e7 0%,#dcdcda 55%,#6b4a36 70%,#f0f0ee 100%)" role="img" aria-label="Minimal interior with a potted plant on a wooden cabinet and a round mirror">
    <span class="work-label">Classic Elegance<br><b>Timeless Luxury</b></span>
  </div>
  <div class="work" style="left:987px;top:249px;height:256px;background:linear-gradient(135deg,#8c8f86 0%,#d9d6cc 40%,#ece9e1 60%,#b8a43c 80%,#9aa190 100%)" role="img" aria-label="Sunlit lounge with a cream armchair and yellow cushion">
    <span class="work-label">The Oasis<br><b>Desert Oasis Luxury</b></span>
  </div>
</section>

<section class="section faq">
  <span class="badge" style="top:64px">Frequently Asked Questions</span>
  <h2 class="heading" style="top:79px">Your Questions, Our Expertise:<br>Navigating the Path to Clarity.</h2>
  <p class="lead" style="top:175px">Here are some FAQs to provide answers to your questions.</p>
  <div class="faq-box">
    <div class="faq-item" style="top:0;height:120px">
      <span class="faq-q" style="top:29px">How do I get started with a custom home project?</span>
      <span class="faq-toggle" style="top:31px"></span>
      <p class="faq-a">To begin your custom home journey, simply reach out to us through our contact page or by calling us directly.<br>We'll set up an initial consultation to discuss your vision, needs, and project details.</p>
    </div>
    <div class="faq-item" style="top:120px"><span class="faq-q" style="left:3px;top:17px">What sets your custom homes apart from others?</span><span class="faq-toggle plus" style="top:19px"></span></div>
    <div class="faq-item" style="top:178px"><span class="faq-q" style="top:17px">Can I see examples of your previous projects?</span><span class="faq-toggle plus" style="top:19px"></span></div>
    <div class="faq-item" style="top:236px"><span class="faq-q" style="top:17px">How long does it take to build a custom home?</span><span class="faq-toggle plus" style="top:19px"></span></div>
    <div class="faq-item" style="top:294px;border-bottom:none"><span class="faq-q" style="top:17px">What is the cost of building a custom home?</span><span class="faq-toggle plus" style="top:19px"></span></div>
  </div>
</section>

<section class="section contact">
  <span class="badge" style="top:64px">Contact Us</span>
  <h2 class="heading" style="top:78px">Your Vision, Our Connection:<br>Reach Out to Begin Your Journey.</h2>
  <p class="lead" style="top:174px">Ready to turn your dream home into a reality?<br>We're here to assist you every step of the way.</p>
  <h3 class="sub-heading" style="top:243px">Contact Information</h3>
  <div class="info-bar">
    <div class="info" style="left:32px">
      <span class="info-icon"><svg width="18" height="18" viewBox="0 0 18 18" fill="#0f3b3a"><path d="M4 2h3l1.5 4-2 1.3a9 9 0 0 0 4.2 4.2L12 9.5l4 1.5v3a2 2 0 0 1-2 2A12 12 0 0 1 2 4a2 2 0 0 1 2-2z"/></svg></span>
      <div><small>Phone Number</small><strong>480 555 0192</strong></div>
    </div>
    <div class="info" style="left:233px">
      <span class="info-icon"><svg width="18" height="18" viewBox="0 0 18 18"><rect x="2" y="4" width="14" height="10" rx="1.5" fill="#0f3b3a"/><path d="M2.5 5 9 10l6.5-5" fill="none" stroke="#fff" stroke-width="1.2"/></svg></span>
      <div><small>Email Address</small><strong>hello@stoneleighhomes.com</strong></div>
    </div>
    <div class="info" style="left:494px;top:21px">
      <span class="info-icon"><svg width="18" height="18" viewBox="0 0 18 18"><path d="M9 1.5a5.5 5.5 0 0 1 5.5 5.5c0 4-5.5 9.5-5.5 9.5S3.5 11 3.5 7A5.5 5.5 0 0 1 9 1.5z" fill="#0f3b3a"/><circle cx="9" cy="7" r="2" fill="#fff"/></svg></span>
      <div><small>Location</small><strong>4820 Desert Willow Lane,<br>Phoenix, Arizona, USA</strong></div>
    </div>
  </div>
  <h3 class="sub-heading" style="top:447px">Send Us a Message</h3>
  <form class="form">
    <span class="field-label" style="left:31px;top:34px">Full name</span>
    <span class="field" style="left:31px;top:50px;width:283px">John B...</span>
    <span class="field-label" style="left:326px;top:34px">Email Address</span>
    <span class="field" style="left:326px;top:50px;width:283px">info@stoneleigh.com</span>
    <span class="field-label" style="left:31px;top:96px">Message</span>
    <span class="field" style="left:31px;top:111px;width:578px;height:93px;padding:14px 20px">Hey there Stoneleigh team...</span>
    <span class="submit">SUBMIT</span>
  </form>
</section>

<footer class="section footer">
  <div class="foot-links" style="left:225px">Home<br>Our Services<br>About Stoneleigh<br>Portfolio</div>
  <div class="foot-links" style="left:359px">Testimonials<br>Contact Us<br>Terms &amp; Conditions<br>Privacy &amp; Policy</div>
  <p class="newsletter">Subscribe to our Newsletter to<br>stay always updated!</p>
  <div class="subscribe">E-Mail<span class="btn btn-blue">SIGN UP</span></div>
  <div class="socials"><span></span><span></span><span></span><span></span></div>
  <div class="foot-rule"></div>
  <div class="brand foot-brand"><span class="brand-dot"></span>STONELEIGH</div>
  <p class="copyright">©Stoneleigh Homes All Rights Reserved</p>
</footer>

</body>
</html>
```